Business Card Design

redesign of card and recreation of logo based on image provided. the business is located in new york so the Brooklyn Bridge figures prominently in the scheme. product should be very clean.

Industry/Entity Type

Real Estate

Contact Information for Business Card

Wendell Ortwick 318 Tamsin Street Brooklyn, New York 11409 wendell@qorvane.com Mobile: 917-555-0143

Colors
cadf82
1b1b1b
ffffff

Requirements
Nice to have
• Brooklyn Bridge

```html
<!DOCTYPE html>
<html lang="en">
<head>
<meta charset="UTF-8">
<title>Ortwick &amp; Partners — Business Card</title>
<link rel="stylesheet" href="https://fonts.googleapis.com/css2?family=Open+Sans:wght@400;600;700&display=swap">
<style>
  :root {
    --stage: #141414;
    --card-white: #ffffff;
    --card-grey: #7a7a7a;
    --tab-grey: #777777;
    --accent-olive: #9a9524;
    --text-grey: #616161;
    --logo-grey: #7a7a7a;
    --white: #ffffff;
  }
  html, body {
    margin: 0;
    padding: 0;
    width: 1200px;
    height: 900px;
    overflow: hidden;
    background: var(--stage);
    font-family: "Open Sans", Arial, sans-serif;
  }
  .canvas {
    position: relative;
    width: 1200px;
    height: 900px;
    background: var(--stage);
  }
  .card {
    position: absolute;
    top: 170px;
    width: 347px;
    height: 561px;
    overflow: hidden;
  }
  .card--front {
    left: 259px;
    background: var(--card-white);
  }
  .card--back {
    left: 631px;
    background: var(--card-grey);
  }
  .card__tab {
    position: absolute;
    left: 102px;
    width: 143px;
    background: var(--tab-grey);
  }
  .card__tab--top { top: 0; height: 30px; }
  .card__tab--bottom { bottom: 0; height: 28px; }

  .brand {
    position: absolute;
    left: 0;
    width: 100%;
    text-align: center;
  }
  .brand__mark {
    display: block;
    margin: 0 auto 14px;
    width: 54px;
    height: 54px;
    border-radius: 50%;
  }
  .brand__name {
    font-size: 21px;
    font-weight: 400;
    letter-spacing: 0.5px;
    text-transform: uppercase;
    margin: 0;
  }
  .card--front .brand { top: 145px; }
  .card--front .brand__mark { background: var(--logo-grey); }
  .card--front .brand__name { color: var(--accent-olive); }
  .card--back .brand { top: 230px; }
  .card--back .brand__mark { background: var(--white); }
  .card--back .brand__name { color: var(--white); }

  .contact {
    position: absolute;
    top: 304px;
    left: 0;
    width: 100%;
    text-align: center;
    color: var(--text-grey);
  }
  .contact__name {
    margin: 0;
    font-size: 18px;
    font-weight: 600;
    color: var(--accent-olive);
    text-transform: uppercase;
    line-height: 24px;
  }
  .contact__address {
    margin: 17px 0 0;
    font-size: 15px;
    line-height: 20px;
    font-style: normal;
  }
  .contact__lines {
    list-style: none;
    margin: 19px 0 0;
    padding: 0;
    font-size: 15px;
    line-height: 20px;
  }
  .contact__line {
    display: flex;
    align-items: center;
    justify-content: center;
    gap: 9px;
  }
  .contact__icon {
    width: 11px;
    height: 11px;
    fill: var(--accent-olive);
  }
</style>
</head>
<body>
<main class="canvas">
  <section class="card card--front" aria-label="Business card front">
    <div class="card__tab card__tab--top"></div>

    <div class="brand">
      <span class="brand__mark"></span>
      <p class="brand__name">Ortwick &amp; Partners</p>
    </div>

    <div class="contact">
      <h1 class="contact__name">Wendell Ortwick</h1>
      <address class="contact__address">
        318 Tamsin Street<br>
        Brooklyn, New York 11409
      </address>
      <ul class="contact__lines">
        <li class="contact__line">
          <svg class="contact__icon" viewBox="0 0 12 12" aria-hidden="true">
            <path d="M1 4 C1 2 3 1 6 1 C9 1 11 2 11 4 L8.5 4.5 L8 3 L4 3 L3.5 4.5 Z M2.5 6 L4 4.5 L8 4.5 L9.5 6 L10 11 L2 11 Z"/>
          </svg>
          <span>917-555-0143</span>
        </li>
        <li class="contact__line">
          <svg class="contact__icon" viewBox="0 0 12 12" aria-hidden="true">
            <path d="M1 3 L11 3 L11 10 L1 10 Z M1.6 3.6 L6 7 L10.4 3.6" stroke="#ffffff" stroke-width="0.9"/>
          </svg>
          <span>wendell@qorvane.com</span>
        </li>
      </ul>
    </div>

    <div class="card__tab card__tab--bottom"></div>
  </section>

  <section class="card card--back" aria-label="Business card back">
    <div class="brand">
      <span class="brand__mark"></span>
      <p class="brand__name">Ortwick &amp; Partners</p>
    </div>
  </section>
</main>
</body>
</html>
```